Lom Consulting -New consulting business in architecture, urban planning, and real estate development

We need a stationery design, including logo, business cards, etc, work for a new consulting business that works in the world of architectural, urban planning and real estate development.

The name of the company is "Lom Consulting". Lom is my last name but it of course also has the meaning 'cool' and 'hip'.

Target Market(s)

The business will provide boutique consulting services to high end clients that may include property developers, cities, etc.

Industry/Entity Type

Consultant

Contact Information for Business Card

LOM Consulting
First Name Last Name
Title
Phone number
Address
Website
Optional: Twitter handle

Logo Text

LOM Consulting

Font styles to use
Sans Serif

Colors

Designer to choose colors to be used in the design.

Requirements
Must have
• Simple design
• Easy to read font
• Modern
• Elegance
• Nice font that can be used for future reports, letters, etc.
• Good colour scheme that allows for the elegance to come through
Should not have
• Complex design ideas
• Complex logos
• Not a corporate feel and look

```html
<!DOCTYPE html>
<html lang="en">
<head>
<meta charset="utf-8">
<title>Lom Consulting — Letterhead</title>
<link href="https://fonts.googleapis.com/css2?family=Questrial&family=Montserrat:wght@400;600&display=swap" rel="stylesheet">
<style>
  :root {
    --backdrop: #ebebeb;
    --paper: #f7f7f7;
    --gold: #b1912c;
    --gold-dark: #9c7f24;
    --ink: #2f2f2f;
    --ink-soft: #5a5a5a;
    --body-grey: #6b6b6b;
    --divider: #b5b5b5;
  }
  * { box-sizing: border-box; margin: 0; padding: 0; }
  html, body {
    width: 1200px; height: 1118px; overflow: hidden;
    background: var(--backdrop);
  }
  .letterhead {
    position: absolute; left: 216px; top: 20px;
    width: 767px; height: 1078px;
    background: var(--paper);
    box-shadow: 0 1px 4px rgba(0,0,0,0.12);
    font-family: "Questrial", sans-serif;
  }
  .header-band {
    position: absolute; left: 0; top: 0; width: 100%; height: 185px;
    background: linear-gradient(90deg, var(--gold-dark), var(--gold) 30%, var(--gold) 70%, var(--gold-dark));
  }
  .brand-name {
    position: absolute; left: 0; top: 38px; width: 100%;
    text-align: center; color: #ffffff;
    font-family: "Questrial", sans-serif; font-weight: 400;
  }
  .brand-name .brand-main { display: block; font-size: 92px; line-height: 96px; letter-spacing: 2px; }
  .brand-name .brand-sub { display: block; font-size: 14px; letter-spacing: 6px; margin-top: 4px; padding-left: 6px; }
  .recipient {
    position: absolute; left: 73px; top: 300px;
    font-size: 14px; line-height: 17.5px; color: var(--ink-soft); letter-spacing: 0.3px;
  }
  .recipient .name, .recipient .role { color: var(--ink); font-family: "Montserrat", sans-serif; font-weight: 600; font-size: 13.5px; }
  .letter-date {
    position: absolute; right: 70px; top: 351px;
    font-size: 14px; color: var(--ink-soft); letter-spacing: 0.3px;
  }
  .letter-body {
    position: absolute; left: 57px; top: 430px; width: 652px;
    font-family: "Montserrat", sans-serif; font-size: 11px; line-height: 23px;
    color: var(--body-grey); text-align: justify;
  }
  .letter-body p { text-indent: 13px; margin-bottom: 23px; }
  .footer {
    position: absolute; left: 0; bottom: 46px; width: 100%;
    font-family: "Montserrat", sans-serif; font-size: 10.5px; color: var(--ink);
    text-align: center;
  }
  .footer .company { font-weight: 600; }
  .footer-address { margin-bottom: 10px; }
  .contact-row { display: flex; justify-content: center; align-items: center; }
  .contact-item { display: flex; align-items: center; gap: 6px; padding: 0 9px; }
  .contact-item + .contact-item { border-left: 1px solid var(--divider); }
  .contact-item svg { width: 13px; height: 13px; fill: none; stroke: var(--gold); stroke-width: 1.4; }
</style>
</head>
<body>
<main class="letterhead">
  <header class="header-band" role="img" aria-label="Gold band with an ornamental mandala pattern">
    <div class="brand-name">
      <span class="brand-main">LOM</span>
      <span class="brand-sub">CONSULTING</span>
    </div>
  </header>

  <address class="recipient" style="font-style:normal">
    <div class="name">MR. Daniel HARTLEY</div>
    <div class="role">Managing Director</div>
    <div>12/40 Cedar Court</div>
    <div>Oregon - 987654321</div>
  </address>

  <div class="letter-date">Date : 01 July 2018</div>

  <section class="letter-body">
    <p>Lorem ipsum dolor sit amet, justo platonem in per, dicant constituto ne eam. Aeque persecuti sit ea, at vis commodo tractatos vituperata, sea an albucius forensibus. Wisi quodsi id qui, duo tempor aliquam assentior eu, no diceret tibique definiebas mei. Id nec noster facilisi mandamus.</p>
    <p>Nullam definiebas signiferumque pro te, vel mutat lobortis conceptam in. Usu justo minimum an, ne regione sanctus praesent usu, eam ut adipisci volutpat. Vel odio tibique consequat ne, in dicit gubergren appellantur vis, quo ei omnis elitr. Qui ne enim dictas dissentiet, pro nulla quodsi deseruisse te. Vide prima eloquentiam pro ei, agam dicta in pro, eu persius propriae constituam sea. Ius ut iriure oblique laboramus, cu sed fugit commune invenire, viris repudiandae ex vis.Nullam definiebas signiferumque pro te, vel mutat lobortis conceptam in. Usu justo minimum an, ne regione sanctus praesent usu, eam ut adipisci volutpat. Vel odio tibique consequat ne, in dicit gubergren appellantur vis, quo ei omnis elitr. Qui ne enim dictas dissentiet, pro nulla quodsi deseruisse te. Vide prima eloquentiam pro ei, agam dicta in pro, eu persius propriae constituam sea. Ius ut iriure oblique laboramus, cu sed fugit commune invenire, viris repudiandae ex vis.Nullam definiebas signiferumque pro te, vel mutat lobortis conceptam in. Usu justo minimum an, ne regione sanctus praesent usu, eam ut adipisci volutpat. Vel odio tibique consequat ne, in dicit gubergren appellantur vis, quo ei omnis elitr. Qui ne enim dictas dissentiet, pro nulla quodsi deseruisse te. Vide prima eloquentiam pro ei, agam dicta in pro, eu persius propriae constituam sea. Ius ut iriure oblique laboramus, cu sed fugit commune invenire, viris repudiandae ex vis.</p>
  </section>

  <footer class="footer">
    <div class="footer-address"><span class="company">Lom Consulting</span> - 418 N Maple Avenue, Fairview, OR 97024</div>
    <div class="contact-row">
      <span class="contact-item">
        <svg viewBox="0 0 16 16" aria-hidden="true"><path d="M3 2 L6 2 L7 5 L5.5 6.5 Q7 9.5 9.5 10.5 L11 9 L14 10 L14 13 Q8 14 4.5 10 Q2 7 3 2 Z" fill="var(--gold)" stroke="none"/></svg>
        000 000 0000
      </span>
      <span class="contact-item">
        <svg viewBox="0 0 16 16" aria-hidden="true"><rect x="1.5" y="3.5" width="13" height="9"/><path d="M1.5 3.5 L8 9 L14.5 3.5"/></svg>
        info@lomconsulting.com
      </span>
      <span class="contact-item">
        <svg viewBox="0 0 16 16" aria-hidden="true"><circle cx="8" cy="8" r="6.3"/><ellipse cx="8" cy="8" rx="2.8" ry="6.3"/><path d="M1.7 8 H14.3 M2.8 4.8 H13.2 M2.8 11.2 H13.2"/></svg>
        www.lomconsulting.com
      </span>
    </div>
  </footer>
</main>
</body>
</html>
```